Electronic Letterhead for The Harborline Partners, LLC

I would like to have an electronic letterhead layout using Word for first and second page letterhead using my previously designed logo. The logo was successfully designed by a designer for the Pixel Bazaar. I would like to only use the "C" portion of the logo on the second page. I would like the designer that designed my logo to be included in the designers that participate in this competition.

Target Market(s)

My clients are typically governmental entities or financial entities

Industry/Entity Type

Electronic

Font styles to use
Sans Serif

Requirements
Must have
• Utilize existing logo
Nice to have
• Fist and second page letterhead design in electronic format (Word)

```html
<!DOCTYPE html>
<html lang="en">
<head>
<meta charset="utf-8">
<title>The Harborline Partners, LLC — Letterhead</title>
<link href="https://fonts.googleapis.com/css2?family=Arimo:wght@400;700&display=swap" rel="stylesheet">
<style>
  :root {
    --workspace: #a7aeb9;
    --titlebar-top: #d4d7db;
    --titlebar-bottom: #b3b8bf;
    --ribbon: #e7e9ec;
    --ribbon-line: #a9adb3;
    --ui-text: #2f2f2f;
    --ui-muted: #5c5f63;
    --tab-accent: #c7b4de;
    --ruler: #f7f7f7;
    --ruler-shade: #c9cdd3;
    --paper: #ffffff;
    --brand-navy: #1d4f8c;
    --body-grey: #8a8a8a;
    --mark-blue: #6f9bd1;
    --hf-line: #9fc0e6;
    --statusbar: #d2d5d9;
  }
  * { box-sizing: border-box; }
  html, body {
    margin: 0;
    padding: 0;
    width: 1200px;
    height: 675px;
    overflow: hidden;
    background: var(--workspace);
    font-family: "Arimo", Arial, sans-serif;
    -webkit-font-smoothing: antialiased;
    -moz-osx-font-smoothing: grayscale;
  }

  /* ---------- application chrome ---------- */
  .toolbar {
    position: absolute; left: 0; top: 0; width: 1200px; height: 13px;
    background: linear-gradient(var(--titlebar-top), var(--titlebar-bottom));
    border-bottom: 1px solid var(--ribbon-line);
    display: flex; align-items: center; gap: 3px; padding-left: 4px;
  }
  .tool-icon { width: 9px; height: 8px; background: #6d7480; border-radius: 1px; opacity: .75; }
  .tool-zoom { margin-left: 6px; width: 22px; height: 9px; background: #fff; border: 1px solid #8d9299;
    font-size: 6px; line-height: 7px; color: var(--ui-text); padding-left: 2px; }
  .search-field {
    position: absolute; right: 22px; top: 2px; width: 90px; height: 9px;
    background: #fff; border: 1px solid #8d9299; border-radius: 5px;
    font-size: 6px; line-height: 7px; color: #888; padding-left: 10px;
  }

  .tab-row {
    position: absolute; left: 0; top: 13px; width: 1200px; height: 14px;
    background: var(--ribbon); border-bottom: 1px solid var(--ribbon-line);
    display: flex; align-items: flex-end; padding-left: 4px; gap: 2px;
  }
  .tab {
    font-size: 6.5px; color: var(--ui-text); padding: 2px 8px; height: 11px;
    border-radius: 2px 2px 0 0; background: #d7dadf; border: 1px solid #b9bdc3; border-bottom: none;
  }
  .tab.is-active { background: #f3f4f6; font-weight: 700; }
  .tab.is-contextual { background: var(--tab-accent); }

  .ribbon {
    position: absolute; left: 0; top: 27px; width: 1200px; height: 32px;
    background: linear-gradient(#f1f2f4, var(--ribbon));
    border-bottom: 1px solid var(--ribbon-line);
  }
  .group-label {
    position: absolute; top: 1px; font-size: 5px; color: var(--ui-muted);
  }
  .font-box {
    position: absolute; left: 3px; top: 8px; width: 52px; height: 9px;
    background: #fff; border: 1px solid #9ba0a6; font-size: 5.5px; line-height: 7px; padding-left: 2px; color: var(--ui-text);
  }
  .size-box {
    position: absolute; left: 58px; top: 8px; width: 16px; height: 9px;
    background: #fff; border: 1px solid #9ba0a6; font-size: 5.5px; line-height: 7px; padding-left: 2px; color: var(--ui-text);
  }
  .button-row { position: absolute; display: flex; gap: 2px; }
  .mini-button { width: 8px; height: 8px; background: #cdd1d6; border: 1px solid #a5aab0; border-radius: 1px; }

  .style-gallery {
    position: absolute; left: 274px; top: 6px; width: 540px; height: 24px;
    background: #fbfbfc; border: 1px solid #b7bbc1;
    display: flex;
  }
  .style-item {
    flex: 1; display: flex; flex-direction: column; align-items: center; justify-content: space-between;
    padding: 2px 0 1px; border-right: 1px solid #e3e5e8;
  }
  .style-sample { font-size: 5.5px; color: #3d3d3d; white-space: nowrap; }
  .style-sample.is-heading { font-family: "Times New Roman", serif; font-size: 7px; color: #3b5f96; font-weight: 700; }
  .style-sample.is-title { font-size: 11px; line-height: 10px; }
  .style-name { font-size: 4.5px; color: var(--ui-muted); white-space: nowrap; }

  .insert-group { position: absolute; left: 832px; top: 6px; display: flex; gap: 6px; }
  .insert-item { display: flex; flex-direction: column; align-items: center; gap: 2px; }
  .insert-icon { width: 14px; height: 12px; border-radius: 2px; background: linear-gradient(#8fb4df, #4f7fbd); }
  .insert-name { font-size: 5px; color: var(--ui-text); }

  .ruler-horizontal {
    position: absolute; left: 13px; top: 59px; width: 1187px; height: 10px;
    background: var(--ruler-shade); border-bottom: 1px solid var(--ribbon-line);
  }
  .ruler-live {
    position: absolute; left: 370px; top: 1px; width: 438px; height: 8px;
    background: repeating-linear-gradient(90deg, transparent 0 9px, #8e939a 9px 10px), var(--ruler);
  }
  .ruler-vertical {
    position: absolute; left: 0; top: 59px; width: 13px; height: 598px;
    background: var(--ruler-shade); border-right: 1px solid var(--ribbon-line);
  }
  .ruler-vertical-live {
    position: absolute; left: 2px; top: 22px; width: 8px; height: 540px;
    background: repeating-linear-gradient(180deg, transparent 0 9px, #8e939a 9px 10px), var(--ruler);
  }

  .statusbar {
    position: absolute; left: 0; top: 657px; width: 1200px; height: 18px;
    background: linear-gradient(#dfe1e4, var(--statusbar));
    border-top: 1px solid var(--ribbon-line);
    font-size: 6px; color: var(--ui-text);
  }
  .view-buttons { position: absolute; left: 4px; top: 4px; display: flex; gap: 2px; }
  .view-button { width: 9px; height: 8px; background: #b9bec5; border: 1px solid #8f949b; }
  .view-button.is-active { background: #5d6673; }
  .status-field { position: absolute; top: 5px; }
  .zoom-slider {
    position: absolute; right: 8px; top: 8px; width: 70px; height: 2px; background: #8f949b;
  }
  .zoom-thumb { position: absolute; left: 40px; top: -3px; width: 6px; height: 8px; background: #f2f2f2; border: 1px solid #7c8189; }

  /* ---------- letter page ---------- */
  .letter-page {
    position: absolute; left: 383px; top: 81px; width: 438px; height: 568px;
    background: var(--paper);
    box-shadow: 0 1px 4px rgba(30, 40, 55, 0.35);
  }
  .brand-block {
    position: absolute; left: 25px; top: 31px;
    display: flex; align-items: center; gap: 9px;
  }
  .brand-mark { width: 58px; height: 58px; display: block; }
  .brand-name { font-size: 12px; font-weight: 700; color: var(--brand-navy); }

  .hf-rule { position: absolute; left: 0; width: 100%; height: 1px; background: var(--hf-line); }
  .hf-tag {
    position: absolute; left: 5px; display: flex; height: 9px;
    font-size: 5.5px; line-height: 7px; color: #3c5d85;
  }
  .hf-tag span {
    background: #eef4fb; border: 1px solid var(--hf-line); padding: 0 3px; margin-right: 2px;
  }
  .format-mark { position: absolute; font-size: 6px; color: var(--mark-blue); line-height: 6px; }

  .letter-body {
    position: absolute; left: 25px; top: 127px; width: 390px;
    font-size: 5.6px; line-height: 6.7px; color: var(--body-grey);
  }
  .letter-body p { margin: 0 0 7px 0; }
  .letter-body .pilcrow { color: var(--mark-blue); margin-left: 2px; }
  .closing { margin-top: 9px !important; }
  .signature-name { margin-top: 27px !important; }
</style>
</head>
<body>
  <div class="toolbar">
    <span class="tool-icon"></span><span class="tool-icon"></span><span class="tool-icon"></span>
    <span class="tool-icon"></span><span class="tool-icon"></span><span class="tool-icon"></span>
    <span class="tool-icon"></span><span class="tool-icon"></span><span class="tool-icon"></span>
    <span class="tool-icon"></span><span class="tool-icon"></span><span class="tool-icon"></span>
    <span class="tool-icon"></span><span class="tool-icon"></span><span class="tool-icon"></span>
    <span class="tool-zoom">153%</span>
    <div class="search-field">Search in Document</div>
  </div>

  <nav class="tab-row">
    <span class="tab is-active">Home</span>
    <span class="tab is-contextual">Header and Footer</span>
    <span class="tab">Layout</span>
    <span class="tab">Document Elements</span>
    <span class="tab">Tables</span>
    <span class="tab">Charts</span>
    <span class="tab">SmartArt</span>
    <span class="tab">Review</span>
  </nav>

  <div class="ribbon">
    <span class="group-label" style="left:58px">Font</span>
    <span class="group-label" style="left:190px">Paragraph</span>
    <span class="group-label" style="left:545px">Styles</span>
    <span class="group-label" style="left:880px">Insert</span>
    <span class="group-label" style="left:918px">Themes</span>
    <div class="font-box">Rockwell (Body)</div>
    <div class="size-box">12</div>
    <div class="button-row" style="left:78px; top:8px">
      <span class="mini-button"></span><span class="mini-button"></span><span class="mini-button"></span><span class="mini-button"></span>
    </div>
    <div class="button-row" style="left:3px; top:20px">
      <span class="mini-button"></span><span class="mini-button"></span><span class="mini-button"></span><span class="mini-button"></span>
      <span class="mini-button"></span><span class="mini-button"></span><span class="mini-button"></span><span class="mini-button"></span>
      <span class="mini-button"></span><span class="mini-button"></span><span class="mini-button"></span><span class="mini-button"></span>
    </div>
    <div class="button-row" style="left:155px; top:8px">
      <span class="mini-button"></span><span class="mini-button"></span><span class="mini-button"></span><span class="mini-button"></span>
      <span class="mini-button"></span><span class="mini-button"></span><span class="mini-button"></span><span class="mini-button"></span>
    </div>
    <div class="button-row" style="left:155px; top:20px">
      <span class="mini-button"></span><span class="mini-button"></span><span class="mini-button"></span><span class="mini-button"></span>
      <span class="mini-button"></span><span class="mini-button"></span><span class="mini-button"></span><span class="mini-button"></span>
    </div>

    <div class="style-gallery">
      <div class="style-item"><span class="style-sample is-heading">AaBbCcE</span><span class="style-name">Heading 1</span></div>
      <div class="style-item"><span class="style-sample is-heading">AaBbCcDc</span><span class="style-name">Heading 2</span></div>
      <div class="style-item"><span class="style-sample">AaBbCcDdEe</span><span class="style-name">Intense Quote</span></div>
      <div class="style-item"><span class="style-sample">AaBbCcDdEe</span><span class="style-name">List Paragraph</span></div>
      <div class="style-item"><span class="style-sample">AaBbCcDdEe</span><span class="style-name">No Spacing</span></div>
      <div class="style-item"><span class="style-sample">AaBbCcDdEe</span><span class="style-name">Quote</span></div>
      <div class="style-item"><span class="style-sample">AaBbCcDdE</span><span class="style-name">Subtitle</span></div>
      <div class="style-item"><span class="style-sample is-title">AaBb</span><span class="style-name">Title</span></div>
      <div class="style-item"><span class="style-sample">AaBbCcDdEe</span><span class="style-name">Subtle Emphs…</span></div>
      <div class="style-item"><span class="style-sample">AaBbCcDdEe</span><span class="style-name">Emphasis</span></div>
      <div class="style-item"><span class="style-sample">AaBbCcDdEe</span><span class="style-name">Intense Emph…</span></div>
      <div class="style-item"><span class="style-sample">AaBbCcDdEe</span><span class="style-name">Strong</span></div>
      <div class="style-item"><span class="style-sample">AaBbCcDdEe</span><span class="style-name">Subtle Refere…</span></div>
      <div class="style-item"><span class="style-sample">AaBbCcDdEe</span><span class="style-name">Intense Refer…</span></div>
      <div class="style-item"><span class="style-sample">AaBbCcDdEe</span><span class="style-name">Book Title</span></div>
    </div>

    <div class="insert-group">
      <div class="insert-item"><span class="insert-icon"></span><span class="insert-name">Text Box</span></div>
      <div class="insert-item"><span class="insert-icon"></span><span class="insert-name">Shape</span></div>
      <div class="insert-item"><span class="insert-icon"></span><span class="insert-name">Picture</span></div>
      <div class="insert-item"><span class="insert-icon"></span><span class="insert-name">Themes</span></div>
    </div>
  </div>

  <div class="ruler-horizontal"><div class="ruler-live"></div></div>
  <div class="ruler-vertical"><div class="ruler-vertical-live"></div></div>

  <main class="letter-page">
    <header class="brand-block">
      <svg class="brand-mark" viewBox="0 0 58 58" aria-hidden="true">
        <circle cx="29" cy="29" r="29" fill="var(--brand-navy)"/>
      </svg>
      <span class="brand-name">The Harborline Partners, LLC</span>
    </header>

    <div class="hf-rule" style="top:96px"></div>
    <div class="hf-tag" style="top:98px"><span>First Page Header</span><span>Close ⊗</span></div>
    <span class="format-mark" style="left:25px; top:112px">¶</span>

    <section class="letter-body">
      <p>Fusce neque mi, consectetuer gravida, convallis ac, varius a, pede. Fusce pellentesque pretium quam. Ut luctus, justo id volutpat iaculis, est diam pulvinar sem, quis bibendum turpis dui eget mauris. Sed in mauris. Ut massa. Pellentesque condimentum felis nec sapien. Integer posuere elit at turpis. Nulla facilisi. Sed sapien ipsum, commodo ut, facilisis vitae, ultrices non, metus. Aenean non nulla. Curabitur molestie volutpat magna. Vestibulum tempor faucibus nisl. Pellentesque vitae enim.<span class="pilcrow">¶</span></p>
      <p>Aliquam rhoncus volutpat mauris. Sed auctor. Donec tincidunt velit at tellus. Donec sed augue eget lacus placerat adipiscing. Ut convallis suscipit nulla. Morbi posuere ullamcorper ligula. Duis sit amet odio nec lorem ornare gravida. Suspendisse ante nulla, gravida quis, eleifend sit amet, placerat eget, purus. Sed egestas magna ut erat. Vivamus euismod, odio id mattis porttitor, lectus nisl consectetuer turpis, ut auctor enim justo euismod nulla. Fusce eget diam vulputate massa tempor tempor.<span class="pilcrow">¶</span></p>
      <p>In ante. Phasellus convallis, nisl in vestibulum facilisis, lacus pede bibendum urna, dapibus pellentesque eros magna sed nibh. Etiam tortor arcu, porta nec, laoreet quis, mollis in, libero. Aenean dapibus est a metus. In sit amet elit. Pellentesque luctus lacus scelerisque arcu. Cras mattis diam. Sed molestie, lectus in bibendum luctus, magna orci luctus quam, et auctor urna diam sit amet ligula. Sed purus dui, suscipit et, malesuada non, consectetuer in, augue. Proin et sapien. Maecenas aliquam, nibh id aliquet tincidunt, ante neque pulvinar mauris, sit amet fermentum nibh augue mollis risus. Mauris porttitor varius mauris. Vivamus in urna et sem accumsan imperdiet. Aenean fringilla, eros tincidunt gravida elementum, justo eros pharetra felis, in rhoncus eros lectus non enim. Phasellus odio tortor, mattis ut, mattis elementum, luctus at, orci.<span class="pilcrow">¶</span></p>
      <p class="closing">Sincerely,<span class="pilcrow">¶</span></p>
      <p class="signature-name">The Harborline Partners LLC<span class="pilcrow">↵</span></p>
    </section>

    <div class="hf-rule" style="top:532px"></div>
    <div class="hf-tag" style="top:524px"><span>First Page Footer</span><span>Close ⊗</span></div>
    <span class="format-mark" style="left:25px; top:535px">¶</span>
  </main>

  <footer class="statusbar">
    <div class="view-buttons">
      <span class="view-button"></span><span class="view-button"></span><span class="view-button"></span>
      <span class="view-button is-active"></span><span class="view-button"></span><span class="view-button"></span>
    </div>
    <span class="status-field" style="left:70px">Print Layout View</span>
    <span class="status-field" style="left:135px">Sec&nbsp;&nbsp;&nbsp;1</span>
    <span class="status-field" style="left:170px">Pages:&nbsp;&nbsp;&nbsp;1 of 1</span>
    <span class="status-field" style="left:1080px">153%</span>
    <div class="zoom-slider"><span class="zoom-thumb"></span></div>
  </footer>
</body>
</html>
```